Offshore Energy Projects Management Consultancy needs a business card design

Logo available. We provide teams to deliver engineering consultancy, project management and delivery teams mainly in the offshore renewables sector. The company is all about bringing the right people to a project to deliver the scope.

The business card will be used for all staff.

The business card should be quite simple, vibrant and uncluttered but convey experience, enthusiasm and integration.

Target Market(s)

Energy Project Developers and Tier 1 construction companies

Contact Information for Business Card

Logo should be on the back of the card. I'm happy for the designer to play with the colour of the logo and background colour.

Front of the card should convey all the must have information in a clear and professional manner but without being overly traditional.

Colors

Designer to choose colors to be used in the design.

Requirements
Must have
• Land Line Tel Number, Mobile Tel Number, Email, business address, web address.

```html
<!DOCTYPE html>
<html lang="en">
<head>
<meta charset="utf-8">
<title>Seaward Delivery Group – Business Card</title>
<link rel="stylesheet" href="https://fonts.googleapis.com/css2?family=Montserrat:wght@500;600;700&family=Questrial&display=swap">
<style>
  :root {
    --deep-blue: #1c75bc;
    --sky-blue: #27a9e1;
    --swoosh-grey: #a3a3a3;
    --paper: #ffffff;
    --ink: #111111;
    --backdrop: #ece6df;
  }
  html, body {
    margin: 0;
    padding: 0;
    width: 1200px;
    height: 1200px;
    overflow: hidden;
    background: var(--backdrop);
  }
  .canvas {
    position: relative;
    width: 1200px;
    height: 1200px;
  }
  .card {
    position: absolute;
    left: 196px;
    width: 786px;
    height: 450px;
    box-shadow: 0 18px 30px rgba(0,0,0,0.18);
  }
  .card--back { top: 76px; }
  .card--front { top: 568px; }
  .card svg { display: block; width: 786px; height: 450px; }

  .brand-name {
    font-family: "Montserrat", sans-serif;
    font-weight: 600;
    letter-spacing: 1px;
  }
  .social-label {
    font-family: "Montserrat", sans-serif;
    font-weight: 500;
    font-size: 19px;
    fill: var(--paper);
  }
  .person-first {
    font-family: "Questrial", sans-serif;
    font-size: 72px;
    fill: var(--ink);
  }
  .person-last {
    font-family: "Montserrat", sans-serif;
    font-weight: 700;
    font-size: 66px;
    fill: var(--ink);
  }
  .person-role {
    font-family: "Questrial", sans-serif;
    font-size: 40px;
    letter-spacing: 8px;
    fill: var(--deep-blue);
  }
  .contact-line {
    font-family: "Questrial", sans-serif;
    font-size: 33px;
    fill: var(--ink);
  }
  .address-line {
    font-family: "Questrial", sans-serif;
    font-size: 31px;
    fill: var(--ink);
  }
</style>
</head>
<body>
<main class="canvas">

  <!-- Back of card: brand side -->
  <section class="card card--back" aria-label="Business card, brand side">
    <svg viewBox="0 0 1266 724" xmlns="http://www.w3.org/2000/svg">
      <rect class="panel-top" width="1266" height="724" fill="var(--deep-blue)"/>
      <path class="wave-white" fill="var(--paper)"
        d="M420,520 C560,560 700,590 800,590 C1000,590 1150,510 1266,437 L1266,724 L420,724 Z"/>
      <path class="wave-grey" fill="var(--swoosh-grey)"
        d="M0,443 C220,450 420,505 600,560 C740,600 830,608 920,606 C1080,602 1190,540 1266,495 L1266,724 L0,724 Z"/>
      <path class="wave-blue" fill="var(--sky-blue)"
        d="M0,462 C220,470 420,520 600,575 C740,615 830,628 920,626 C1080,622 1190,565 1266,515 L1266,724 L0,724 Z"/>

      <text class="brand-name" x="633" y="330" text-anchor="middle" font-size="62" fill="var(--paper)">SEAWARD</text>
      <text class="brand-name" x="633" y="400" text-anchor="middle" font-size="62" fill="var(--paper)">DELIVERY GROUP</text>

      <text class="social-label" x="52" y="594">FIND US ON SOCIAL MEDIA!</text>
      <g class="social-slots" fill="none" stroke="var(--paper)" stroke-width="4">
        <circle cx="89" cy="646" r="29"/>
        <circle cx="180" cy="646" r="29"/>
        <circle cx="271" cy="646" r="29"/>
      </g>
    </svg>
  </section>

  <!-- Front of card: contact side -->
  <section class="card card--front" aria-label="Business card, contact side">
    <svg viewBox="0 0 1266 724" xmlns="http://www.w3.org/2000/svg">
      <rect class="panel" width="1266" height="724" fill="var(--paper)"/>
      <path class="corner-blue" fill="var(--sky-blue)"
        d="M0,0 L1000,0 C820,48 620,42 420,72 C260,98 110,150 0,192 Z"/>
      <path class="corner-grey" fill="var(--swoosh-grey)"
        d="M0,210 C150,132 400,72 650,60 C400,82 160,160 0,263 Z"/>
      <path class="foot-grey" fill="var(--swoosh-grey)"
        d="M1266,512 C1100,610 900,670 660,683 C900,678 1100,622 1266,560 Z"/>
      <path class="foot-blue" fill="var(--sky-blue)"
        d="M1266,575 C1100,650 900,690 700,700 C550,705 450,712 370,724 L1266,724 Z"/>

      <text class="brand-name" x="300" y="390" text-anchor="middle" font-size="38" fill="var(--deep-blue)">SEAWARD</text>
      <text class="brand-name" x="300" y="434" text-anchor="middle" font-size="38" fill="var(--deep-blue)">DELIVERY GROUP</text>

      <text x="870" y="170" text-anchor="middle">
        <tspan class="person-first">Callum </tspan><tspan class="person-last">Ardley</tspan>
      </text>
      <text class="person-role" x="872" y="215" text-anchor="middle">DIRECTOR</text>

      <g class="contact-icons">
        <circle cx="666" cy="306" r="33" fill="var(--sky-blue)"/>
        <rect x="656" y="289" width="20" height="34" rx="3" fill="none" stroke="var(--paper)" stroke-width="4"/>
        <circle cx="666" cy="393" r="33" fill="var(--sky-blue)"/>
        <rect x="648" y="381" width="36" height="24" rx="2" fill="none" stroke="var(--paper)" stroke-width="4"/>
        <path d="M649,383 L666,396 L683,383" fill="none" stroke="var(--paper)" stroke-width="4"/>
        <circle cx="666" cy="481" r="33" fill="var(--sky-blue)"/>
        <g fill="none" stroke="var(--paper)" stroke-width="3">
          <circle cx="666" cy="481" r="17"/>
          <ellipse cx="666" cy="481" rx="7" ry="17"/>
          <line x1="649" y1="481" x2="683" y2="481"/>
          <line x1="652" y1="472" x2="680" y2="472"/>
          <line x1="652" y1="490" x2="680" y2="490"/>
        </g>
      </g>

      <text class="contact-line" x="722" y="300">+44 1632 960 418</text>
      <text class="contact-line" x="722" y="342">+44 1632 960 522</text>
      <text class="contact-line" x="722" y="405">hello@seaward.group</text>
      <text class="contact-line" x="722" y="492">www.seaward.group</text>

      <text class="address-line" x="802" y="571" text-anchor="middle">Harbour Point House, 27 Quay Road,</text>
      <text class="address-line" x="802" y="608" text-anchor="middle">Portmere, PM4 2QT</text>
    </svg>
  </section>

</main>
</body>
</html>
```